Book Flyer

I want a flyer that we can use to promote this book to educators and to leaders....below is a sample flyer but I want something bold and creative and different from this....it can be completely different from what is attached. I want to be a WOW to increase sales. Please include pic of book and how folks can get a copy....I've given you a few pics but please be creative ....looking for a wow.

```html
<!DOCTYPE html>
<html lang="en">
<head>
<meta charset="utf-8">
<title>Purposeful Excellence – Book Flyer</title>
<link rel="stylesheet" href="https://fonts.googleapis.com/css2?family=Bebas+Neue&family=Oswald:wght@500&family=Playfair+Display:wght@900&family=Poppins:ital,wght@0,300;0,400;0,600;0,700;1,600;1,700&display=swap">
<style>
  :root {
    --navy: #141a3a;
    --navy-deep: #0f1430;
    --red: #e84142;
    --yellow: #fcd116;
    --blue: #2a7fc4;
    --ink: #1c1c1c;
    --white: #ffffff;
  }
  * { margin: 0; padding: 0; box-sizing: border-box; }
  html, body { width: 854px; height: 1200px; overflow: hidden; background: var(--white); }
  .flyer { position: relative; width: 854px; height: 1200px; overflow: hidden; font-family: "Poppins", sans-serif; background: var(--white); }
  .backdrop { position: absolute; inset: 0; }

  .title-box { position: absolute; left: 52px; top: 62px; width: 381px; height: 95px; background: var(--red); display: flex; align-items: center; justify-content: center; }
  .title-main { font-family: "Bebas Neue", sans-serif; font-size: 104px; line-height: 1; color: var(--white); letter-spacing: 1px; padding-top: 8px; }
  .title-sub { position: absolute; left: 50px; top: 170px; font-family: "Poppins", sans-serif; font-weight: 300; font-size: 47px; line-height: 1; color: var(--yellow); letter-spacing: 1px; }

  .review { position: absolute; left: 52px; top: 245px; width: 335px; color: var(--white); font-size: 16.4px; line-height: 20.6px; text-align: justify; }
  .review .open { font-family: "Playfair Display", serif; font-weight: 900; color: var(--red); font-size: 56px; line-height: 0; position: relative; top: 24px; margin-right: 26px; }
  .review .close { font-family: "Playfair Display", serif; font-weight: 900; color: var(--red); font-size: 56px; line-height: 0; position: relative; top: 26px; margin-left: 4px; }
  .review-by { position: absolute; left: 200px; top: 530px; color: var(--white); font-size: 16.5px; line-height: 21px; }
  .review-by .first { color: var(--yellow); font-style: italic; font-weight: 600; }
  .review-by .last { font-style: italic; font-weight: 600; }
  .review-by .role { display: block; padding-left: 8px; }

  .strategies-bar { position: absolute; left: 293px; top: 778px; width: 485px; height: 37px; background: var(--navy); border-radius: 3px; color: var(--white); font-weight: 600; font-size: 14.6px; display: flex; align-items: center; justify-content: center; }
  .strategies-bar span { color: var(--yellow); margin-right: 4px; }

  .strategy { position: absolute; top: 828px; height: 137px; }
  .strategy.equity { left: 287px; width: 154px; }
  .strategy.change { left: 455px; width: 154px; }
  .strategy.communication { left: 622px; width: 160px; }
  .divider { position: absolute; top: 816px; width: 1px; height: 150px; background: #9a9a9a; }
  .strategy h3 { display: flex; align-items: center; gap: 4px; font-size: 13.8px; font-weight: 600; margin-bottom: 5px; }
  .strategy .icon { width: 23px; height: 23px; border-radius: 3px; display: flex; align-items: center; justify-content: center; }
  .equity h3 { color: var(--red); } .equity .icon { background: var(--red); }
  .change h3 { color: var(--yellow); } .change .icon { background: var(--yellow); }
  .communication h3 { color: var(--blue); } .communication .icon { background: var(--blue); }
  .strategy blockquote { font-size: 11.3px; line-height: 13.2px; color: var(--ink); text-align: justify; }
  .strategy .q { font-family: "Playfair Display", serif; font-weight: 900; font-size: 17px; line-height: 0; position: relative; top: 4px; }
  .equity .q { color: var(--red); } .change .q { color: var(--yellow); } .communication .q { color: var(--blue); }
  .strategy cite { display: block; text-align: right; font-style: italic; font-weight: 700; font-size: 11px; margin-top: 10px; color: var(--ink); }
  .communication cite { text-align: left; padding-left: 6px; }
  .change blockquote, .communication blockquote { padding-right: 4px; }

  .about { position: absolute; left: 232px; top: 977px; width: 622px; height: 171px; background: var(--red); color: var(--white); }
  .about h2 { position: absolute; left: 0; right: 0; top: 16px; text-align: center; font-size: 19.5px; font-weight: 700; color: var(--yellow); }
  .about h2 em { font-weight: 400; font-style: italic; color: var(--white); }
  .about p { position: absolute; left: 66px; width: 522px; top: 44px; text-align: center; font-size: 13.6px; line-height: 17px; }

  .portrait { position: absolute; left: 52px; top: 749px; width: 225px; height: 451px; }

  .footer { position: absolute; left: 238px; top: 1148px; width: 616px; height: 52px; display: flex; align-items: center; font-family: "Oswald", sans-serif; color: var(--blue); font-size: 19px; }
  .footer .cta { font-weight: 500; letter-spacing: 0.3px; }
  .footer .contact { display: flex; align-items: center; gap: 5px; font-weight: 400; }
  .footer .web { margin-left: 22px; }
  .footer .mail { margin-left: 28px; }
</style>
</head>
<body>
<div class="flyer">
  <svg class="backdrop" width="854" height="1200" viewBox="0 0 854 1200" aria-hidden="true">
    <defs>
      <linearGradient id="navyFade" x1="0" y1="0" x2="0" y2="1">
        <stop offset="0" stop-color="#151b3d"/>
        <stop offset="1" stop-color="#1a2347"/>
      </linearGradient>
    </defs>
    <rect width="854" height="760" fill="url(#navyFade)"/>
    <path d="M0,650 C200,690 360,590 440,530 C560,430 700,380 854,470 L854,1200 L0,1200Z" fill="var(--yellow)"/>
    <path d="M0,660 C210,700 370,610 450,555 C570,470 720,440 854,490 L854,1200 L0,1200Z" fill="var(--blue)"/>
    <path d="M0,670 C210,710 380,640 470,600 C560,560 610,640 690,655 C760,660 800,560 854,530 L854,1200 L0,1200Z" fill="var(--red)"/>
    <path d="M0,712 C200,738 370,670 470,635 C560,605 620,705 700,695 C770,685 810,600 854,575 L854,1200 L0,1200Z" fill="var(--white)"/>
    <polygon points="696,137 718,113 728,146" fill="var(--yellow)"/>
    <polygon points="648,201 667,141 712,185" fill="var(--red)"/>
    <polygon points="56,610 104,565 120,629" fill="var(--yellow)"/>
    <polygon points="262,736 289,720 294,752" fill="var(--yellow)"/>
    <polygon points="214,809 231,746 278,790" fill="var(--blue)"/>
    <polygon points="687,761 699,733 717,761" fill="var(--yellow)"/>
    <polygon points="13,1065 37,1040 47,1072" fill="var(--yellow)"/>
    <polygon points="0,1081 31,1110 0,1119" fill="var(--blue)"/>
  </svg>

  <div class="title-box"><h1 class="title-main">PURPOSEFUL</h1></div>
  <div class="title-sub">EXCELLENCE</div>

  <p class="review"><span class="open">“</span>Purposeful Excellence is a book written for all leaders. Dr. Miles Carter speaks from real life experiences that are relatable and from the heart. His leadership steps have helped him develop into one of the most accomplished administrative leaders in the country. The three specific strategies outlined in this pock will transform your leadership skills and help you stay on track to ensure success.<span class="close">”</span></p>
  <p class="review-by">-<span class="first">Helen</span> <span class="last">Garvey</span>,<span class="role">Principal</span></p>

  <svg style="position:absolute;left:0;top:0" width="854" height="1200" viewBox="0 0 854 1200" role="img" aria-label="Book cover of Purposeful Excellence by R. Miles Carter, foreword by Tom Bellamy, with rising arrows artwork">
    <defs>
      <linearGradient id="coverTones" x1="0" y1="0" x2="0.25" y2="1">
        <stop offset="0" stop-color="#1b2a55"/>
        <stop offset="0.38" stop-color="#2d5f9c"/>
        <stop offset="0.42" stop-color="#e84142"/>
        <stop offset="0.62" stop-color="#e84142"/>
        <stop offset="0.66" stop-color="#ffffff"/>
        <stop offset="1" stop-color="#f1f1f1"/>
      </linearGradient>
    </defs>
    <polygon points="748,258 770,268 648,750 636,752" fill="#d9d9d9"/>
    <polygon points="505,218 748,258 636,752 381,654" fill="url(#coverTones)"/>
  </svg>

  <div class="portrait" role="img" aria-label="Portrait photo of the author standing with arms crossed, in a light blue shirt and patterned tie">
    <svg width="225" height="451" viewBox="0 0 225 451" aria-hidden="true">
      <defs>
        <linearGradient id="portraitTones" x1="0" y1="0" x2="0" y2="1">
          <stop offset="0" stop-color="#4a3a32"/>
          <stop offset="0.3" stop-color="#dfe6f1"/>
          <stop offset="0.78" stop-color="#cfd9ea"/>
          <stop offset="0.85" stop-color="#4d4d55"/>
          <stop offset="1" stop-color="#3b3b42"/>
        </linearGradient>
      </defs>
      <path d="M85,0 H150 V120 C195,130 220,150 225,200 V451 H10 V200 C12,150 40,128 85,120Z" fill="url(#portraitTones)"/>
    </svg>
  </div>

  <div class="strategies-bar"><span>3 Fundamental Strategies</span> that Drive Educational Leadership</div>

  <div class="divider" style="left:442px"></div>
  <div class="divider" style="left:609px"></div>

  <section class="strategy equity">
    <h3><span class="icon"><svg width="15" height="14" viewBox="0 0 15 14"><g fill="#fff"><circle cx="2.5" cy="2" r="1.6"/><circle cx="7.5" cy="2" r="1.6"/><circle cx="12.5" cy="2" r="1.6"/><rect x="1" y="4.5" width="3" height="9"/><rect x="6" y="4.5" width="3" height="9"/><rect x="11" y="4.5" width="3" height="9"/></g></svg></span>EQUITY</h3>
    <blockquote><span class="q">“</span>Fariness does not mean everyone gets the same. Fairness means everyone gets what they need.<span class="q">”</span></blockquote>
    <cite>-Nora Whitfield</cite>
  </section>

  <section class="strategy change">
    <h3><span class="icon"><svg width="14" height="14" viewBox="0 0 14 14"><g fill="none" stroke="#fff" stroke-width="1.8"><path d="M2,6 A5,5 0 0 1 11,4"/><path d="M12,8 A5,5 0 0 1 3,10"/></g><polygon points="11,1 12.5,5 8.5,5" fill="#fff"/><polygon points="3,13 1.5,9 5.5,9" fill="#fff"/></svg></span>CHANGE</h3>
    <blockquote><span class="q">“</span>If you do not change direction, you may end up where you are heading.<span class="q">”</span></blockquote>
    <cite style="margin-top:24px">-Elias Monroe</cite>
  </section>

  <section class="strategy communication">
    <h3><span class="icon"><svg width="15" height="14" viewBox="0 0 15 14"><g fill="#fff"><circle cx="4" cy="4" r="2"/><circle cx="11" cy="4" r="2"/><rect x="1.5" y="7" width="5" height="6" rx="1.5"/><rect x="8.5" y="7" width="5" height="6" rx="1.5"/></g></svg></span>COMMUNICATION</h3>
    <blockquote><span class="q">“</span>The single bigge problem in communica­tion is th illusion that is has taken place.<span class="q">”</span></blockquote>
    <cite>-Greta Lindqvist</cite>
  </section>

  <section class="about">
    <h2>ABOUT <em>Dr. Carter</em></h2>
    <p>Distinguished as a vibrant, visionary, and innovative leader who recognizes that humility is the most important trait a leader can possess, Dr. Carter uses his prior experiences in business, education, and nonprofit to assist organization leaders from all industries build internal leadership capacity, including strategy &amp; talent management and development to maximize organizational potential and success.</p>
  </section>

  <footer class="footer">
    <span class="cta">TO GET YOUR COPY</span>
    <span class="contact web"><svg width="22" height="22" viewBox="0 0 22 22" aria-hidden="true"><g fill="none" stroke="var(--red)" stroke-width="1.6"><circle cx="11" cy="11" r="9"/><ellipse cx="11" cy="11" rx="4" ry="9"/><line x1="2" y1="11" x2="20" y2="11"/></g></svg>www.drmilescarter.com</span>
    <span class="contact mail"><svg width="22" height="16" viewBox="0 0 22 16" aria-hidden="true"><rect x="1" y="1" width="20" height="14" fill="none" stroke="var(--red)" stroke-width="1.8"/><polyline points="1,1 11,9 21,1" fill="none" stroke="var(--red)" stroke-width="1.8"/></svg>info@drmilescarter.com</span>
  </footer>
</div>
</body>
</html>
```